Corvanta Business cards template

We're looking for something modern and elegant. We are a reseller of technology (computers, datacenter, etc). Color theme would be "only" white with the incorporation of the blue that's present on our website (Corvanta.com) and logo file. We would like for the card to provide all the necessary info for the specific person (Phone#, fax#, email, name, website URL) . I'm attaching the logo file to this request. Please have it show Montreal/New York somewhere, without providing specific addresses.

Target Market(s)

All b2b

Industry/Entity Type

Business

Contact Information for Business Card

Please have the color scheme be represented by only the white and blue from our website (Corvanta.com) and logo. We would like to logo on the card, but not big and overwhelming. This card will be used as a template for anybody within the company, it should display the user's name, phone#, fax#, email, job title and website URL. Please have it show Montreal/New York somewhere, without providing our specific addresses. Really, we're looking for a clean, simple and elegant look.

Font styles to use
Serif

Requirements
Must have
• Please see card details
Nice to have
• Please see card details
Should not have
• Anything tacky or tagline.

```html
<!DOCTYPE html>
<html lang="en">
<head>
<meta charset="utf-8">
<title>Corvanta Business Card</title>
<link href="https://fonts.googleapis.com/css2?family=Crimson+Pro:wght@400;500;700&display=swap" rel="stylesheet">
<style>
  :root {
    --page-bg: #e4e5e7;
    --card-bg: #ffffff;
    --brand-blue: #1a74c4;
    --name-blue: #1c5fae;
    --ink: #2b2b2b;
    --muted-ink: #555b63;
    --card-shadow: rgba(0, 0, 0, 0.22);
  }
  * { margin: 0; padding: 0; box-sizing: border-box; }
  html, body {
    width: 1200px;
    height: 1000px;
    overflow: hidden;
    background: var(--page-bg);
    font-family: "Crimson Pro", serif;
  }
  .card-set {
    position: absolute;
    top: 345px;
    left: 40px;
    display: flex;
    gap: 40px;
  }
  .card {
    position: relative;
    width: 540px;
    height: 309px;
    background: var(--card-bg);
    box-shadow: 0 4px 14px var(--card-shadow);
  }
  .wordmark {
    display: flex;
    align-items: center;
    gap: 10px;
    color: var(--brand-blue);
    font-weight: 400;
    font-size: 40px;
    line-height: 1;
  }
  .wordmark-dot {
    width: 13px;
    height: 13px;
    border-radius: 50%;
    background: var(--brand-blue);
  }
  .card-front .wordmark {
    position: absolute;
    left: 42px;
    top: 68px;
  }
  .holder {
    position: absolute;
    left: 42px;
    top: 208px;
  }
  .holder-name {
    color: var(--name-blue);
    font-weight: 700;
    font-size: 20px;
    letter-spacing: 0.6px;
    line-height: 1.1;
  }
  .holder-title {
    color: var(--ink);
    font-weight: 500;
    font-size: 11px;
    letter-spacing: 1px;
    margin-top: 3px;
  }
  .locations {
    position: absolute;
    right: 36px;
    top: 236px;
    color: var(--muted-ink);
    font-weight: 500;
    font-size: 11px;
    letter-spacing: 1.4px;
    line-height: 1;
  }
  .rule {
    position: absolute;
    left: 42px;
    right: 36px;
    top: 256px;
    height: 2px;
    background: var(--brand-blue);
  }
  .contact-line {
    position: absolute;
    left: 42px;
    top: 265px;
    color: var(--ink);
    font-size: 13px;
    white-space: nowrap;
  }
  .card-back {
    display: flex;
    align-items: center;
    justify-content: center;
  }
</style>
</head>
<body>
  <main class="card-set">
    <section class="card card-front">
      <div class="wordmark"><span class="wordmark-dot"></span>Corvanta</div>
      <div class="holder">
        <p class="holder-name">DANIEL MERCER</p>
        <p class="holder-title">FOUNDER</p>
      </div>
      <p class="locations">MONTREAL | NEW YORK</p>
      <div class="rule"></div>
      <p class="contact-line">000 000 0000 | 000 000 0000 | info@danielmercer.com | Corvanta.com</p>
    </section>
    <section class="card card-back">
      <div class="wordmark"><span class="wordmark-dot"></span>Corvanta</div>
    </section>
  </main>
</body>
</html>
```